Foldable Bluetooth Headphone Packaging Design

We would like a window box style packaging design for our Foldable Bluetooth Headphone.

We want to use the packaging for 4-5 of our Bluetooth headphone series (enclosed picture of the headphones for reference) and hence we would not like to put any product pictures on the packaging.
Material: E-Flute Paper box
Type: Window Box style
Design features we prefer: Colorful, creative, trendy, High tech.
Requirement: AI file is preferred
Size of Packaging: 170 (L) x 120 (W) x 200 (H) mm

Enclosed are a detailed description along with competitor designs for your reference.

Any further questions, please feel free to ask.

Target Market(s)

25-35 year olds

Industry/Entity Type

Electronics

Colors

Designer to choose colors to be used in the design.

Requirements
Must have
• Trendy Design

```html
<!DOCTYPE html>
<html lang="en">
<head>
<meta charset="UTF-8">
<title>Foldable Bluetooth Headphone Packaging</title>
<link href="https://fonts.googleapis.com/css2?family=Montserrat:wght@400;500;600;700&family=Signika:wght@400;500&display=swap" rel="stylesheet">
<style>
  :root {
    --bg: #1b1c1c;
    --violet-deep: #1c0f4a;
    --violet-mid: #2e1a7a;
    --violet-glow: #4d30a8;
    --side-dark: #0b0724;
    --side-mid: #1e1258;
    --ink-white: #ffffff;
    --ink-grey: #8d8a99;
    --window-edge: rgba(190, 170, 255, 0.35);
  }
  * { margin: 0; padding: 0; box-sizing: border-box; }
  html, body {
    width: 1200px; height: 1200px; overflow: hidden;
    background: var(--bg);
  }
  .packaging {
    position: absolute; left: 90px; top: 260px;
    display: flex; gap: 12px;
  }
  .panel-front {
    position: relative; width: 580px; height: 680px;
    background: radial-gradient(ellipse 60% 45% at 38% 52%, var(--violet-glow) 0%, var(--violet-mid) 55%, var(--violet-deep) 100%);
    overflow: hidden;
  }
  .brand-block {
    position: absolute; top: 84px; left: 40px; width: 320px;
    color: var(--ink-white); font-family: 'Montserrat', sans-serif;
    text-align: left; white-space: nowrap;
  }
  .brand-name { font-size: 48px; font-weight: 500; letter-spacing: -1px; line-height: 1; }
  .brand-line { font-size: 22px; font-weight: 500; margin-top: 12px; letter-spacing: -0.3px; }
  .brand-product { font-size: 28px; font-weight: 500; letter-spacing: 9px; margin-top: 2px; }
  .features {
    position: absolute; left: 12px; bottom: 22px; width: 350px;
    color: var(--ink-white); font-family: 'Signika', sans-serif;
  }
  .features-title { font-size: 28px; font-weight: 500; margin-bottom: 8px; }
  .features-list { list-style: none; font-size: 16px; line-height: 29px; white-space: nowrap; }
  .features-list li::before { content: "• "; }
  .window {
    position: absolute; left: 380px; top: 14px; right: 24px; bottom: 14px;
    border: 2px solid var(--window-edge); border-left: none;
    border-radius: 0 26px 26px 0;
    overflow: hidden;
  }
  .window-contents {
    width: 100%; height: 100%;
    background: radial-gradient(ellipse 70% 55% at 30% 50%, #2a1440 0%, #1b0e3c 45%, #241560 100%);
  }
  .panel-side {
    width: 409px; height: 680px;
    background: linear-gradient(90deg, var(--side-dark) 0%, var(--side-mid) 100%);
    display: flex; justify-content: center; align-items: flex-end;
    padding-bottom: 78px;
  }
  .side-title {
    writing-mode: vertical-rl; transform: rotate(180deg);
    color: var(--ink-grey); font-family: 'Montserrat', sans-serif;
    font-weight: 700; line-height: 1; white-space: nowrap;
  }
  .side-title .brand-name { font-size: 54px; font-weight: 700; letter-spacing: 1px; }
  .side-title .brand-line { font-size: 22px; font-weight: 500; margin: 0 0 0 6px; }
  .side-title .brand-product { font-size: 27px; font-weight: 500; letter-spacing: 10px; margin: 0 0 0 4px; }
</style>
</head>
<body>
  <main class="packaging">
    <section class="panel-front">
      <div class="brand-block">
        <div class="brand-name">LOGO TEXT</div>
        <div class="brand-line">FOLDABLE BLUETOOTH</div>
        <div class="brand-product">HEADPHONE</div>
      </div>
      <div class="features">
        <div class="features-title">Features:</div>
        <ul class="features-list">
          <li>Bluetooth V5</li>
          <li>Foldable and Portable</li>
          <li>Exceptional Sound Quality</li>
          <li>Dual Mode wireless or wired connectivity</li>
          <li>Adjustable headband</li>
        </ul>
      </div>
      <div class="window">
        <div class="window-contents" role="img" aria-label="Die-cut window showing the folded headphones inside the box"></div>
      </div>
    </section>
    <section class="panel-side">
      <div class="side-title">
        <div class="brand-name">LOGO TEXT</div>
        <div class="brand-line">FOLDABLE BLUETOOTH</div>
        <div class="brand-product">HEADPHONE</div>
      </div>
    </section>
  </main>
</body>
</html>
```